Brivolo ( A new twist on task management )

We need modern, elegant, and clean (Quillon Design) on screens, buttons, and icons.

It is a (smart) task management application which helps the users to get notified and track task completion hassle free; Using notification profiles they create.

The interface of this application should be very simple and color schemes should be contemporary as long as they don’t make reading short text hard.

Following Quillon Design guidelines, the prefered font style is Roboto

Target Market(s)

Everyone from 13+

Industry/Entity Type

Software

Logo Text

Brivolo

Font styles to use
Other font styles liked:
• Roboto

```html
<!DOCTYPE html>
<html lang="en">
<head>
<meta charset="utf-8">
<title>Brivolo — Active Tasks</title>
<link href="https://fonts.googleapis.com/css2?family=Open+Sans:wght@400;600;700&display=swap" rel="stylesheet">
<style>
  :root {
    --page: #ffffff;
    --header-bg: #bfe6f8;
    --accent: #1e8fd9;
    --accent-dark: #1677bd;
    --divider: #b9dcf1;
    --status-text: #111111;
    --badge: #e53935;
    --avatar: #8a5a4a;
    --fab-icon: #ffffff;
  }
  * { margin: 0; padding: 0; box-sizing: border-box; }
  html, body {
    width: 831px; height: 1200px; overflow: hidden;
    background: var(--page);
    font-family: "Open Sans", Arial, sans-serif;
  }
  .app-screen { position: relative; width: 831px; height: 1200px; background: var(--page); }

  .status-bar {
    position: absolute; top: 0; left: 0; right: 0; height: 30px;
    display: flex; align-items: center; justify-content: space-between;
    padding: 0 14px; font-size: 17px; font-weight: 600; color: var(--status-text);
  }
  .status-left, .status-right { display: flex; align-items: center; gap: 6px; }
  .status-time { position: absolute; left: 50%; transform: translateX(-50%); }

  .top-bar {
    position: absolute; top: 30px; left: 0; right: 0; height: 104px;
    background: var(--header-bg);
    display: flex; align-items: center;
    box-shadow: 0 2px 4px rgba(0,0,0,0.12);
  }
  .back-button { position: absolute; left: 26px; top: 36px; }
  .screen-title {
    position: absolute; left: 90px; top: 34px;
    font-size: 30px; font-weight: 700; color: var(--accent); letter-spacing: 0.5px;
  }
  .search-button { position: absolute; left: 620px; top: 32px; }
  .profile { position: absolute; left: 722px; top: 16px; width: 72px; height: 72px; }
  .profile-photo {
    width: 72px; height: 72px; border-radius: 50%;
    background: radial-gradient(circle at 45% 40%, #d7a48c, var(--avatar) 70%);
    border: 3px solid #ffffff;
  }
  .profile-badge {
    position: absolute; right: -4px; top: -2px; width: 26px; height: 26px;
    border-radius: 50%; background: var(--badge); color: #fff;
    font-size: 16px; font-weight: 700; display: flex; align-items: center; justify-content: center;
    border: 2px solid #fff;
  }

  .task-list { position: absolute; top: 134px; left: 0; right: 0; list-style: none; }
  .task-row {
    position: relative; height: 170px;
    border-bottom: 2px dashed var(--divider);
  }
  .task-state { position: absolute; left: 74px; top: 64px; }
  .task-name {
    position: absolute; left: 118px; top: 60px;
    font-size: 30px; font-weight: 700; color: var(--accent); letter-spacing: 0.5px;
  }
  .task-row.is-running .task-name { left: 134px; top: 40px; }
  .task-row.is-running .task-state { top: 48px; }
  .task-timer {
    position: absolute; left: 134px; top: 86px;
    font-size: 21px; font-weight: 700; color: var(--accent-dark); letter-spacing: 0.5px;
  }
  .task-row.is-running .task-action { top: 44px; }
  .task-action { position: absolute; top: 60px; }
  .action-pin { left: 580px; }
  .action-clock { left: 666px; }
  .action-place { left: 756px; }

  .add-button {
    position: absolute; left: 700px; top: 1046px; width: 96px; height: 96px;
    border-radius: 50%; background: var(--accent);
    box-shadow: 0 3px 8px rgba(0,0,0,0.25);
    display: flex; align-items: center; justify-content: center;
  }
</style>
</head>
<body>
<main class="app-screen">

  <div class="status-bar">
    <div class="status-left">
      <svg width="56" height="12" viewBox="0 0 56 12" aria-hidden="true">
        <circle cx="6" cy="6" r="4.5" fill="#111"/><circle cx="17" cy="6" r="4.5" fill="#111"/>
        <circle cx="28" cy="6" r="4.5" fill="#111"/><circle cx="39" cy="6" r="4.5" fill="#111"/>
        <circle cx="50" cy="6" r="4" fill="none" stroke="#111" stroke-width="1.2"/>
      </svg>
      <span>mobile</span>
      <svg width="22" height="16" viewBox="0 0 22 16" aria-hidden="true">
        <path d="M1 6 A15 15 0 0 1 21 6" fill="none" stroke="#111" stroke-width="2"/>
        <path d="M5 10 A9 9 0 0 1 17 10" fill="none" stroke="#111" stroke-width="2"/>
        <circle cx="11" cy="14" r="2" fill="#111"/>
      </svg>
    </div>
    <span class="status-time">17:45 PM</span>
    <div class="status-right">
      <svg width="12" height="18" viewBox="0 0 12 18" aria-hidden="true">
        <path d="M2 5 L10 13 L6 17 L6 1 L10 5 L2 13" fill="none" stroke="#111" stroke-width="1.6"/>
      </svg>
      <span>100%</span>
      <svg width="44" height="18" viewBox="0 0 44 18" aria-hidden="true">
        <rect x="1" y="1" width="38" height="16" rx="3" fill="none" stroke="#111" stroke-width="1.6"/>
        <rect x="4" y="4" width="32" height="10" rx="1" fill="#111"/>
        <rect x="40" y="6" width="3" height="6" rx="1" fill="#111"/>
      </svg>
    </div>
  </div>

  <header class="top-bar">
    <svg class="back-button" width="40" height="32" viewBox="0 0 40 32" aria-label="Back">
      <path d="M36 16 H5 M17 4 L5 16 L17 28" fill="none" stroke="var(--accent)" stroke-width="4" stroke-linecap="round" stroke-linejoin="round"/>
    </svg>
    <h1 class="screen-title">ACTIVE TASKS</h1>
    <svg class="search-button" width="40" height="40" viewBox="0 0 40 40" aria-label="Search">
      <circle cx="16" cy="16" r="11" fill="none" stroke="var(--accent)" stroke-width="4"/>
      <path d="M24 24 L36 36" stroke="var(--accent)" stroke-width="5" stroke-linecap="round"/>
    </svg>
    <div class="profile">
      <div class="profile-photo" role="img" aria-label="User profile photo"></div>
      <span class="profile-badge">5</span>
    </div>
  </header>

  <ul class="task-list">
    <li class="task-row">
      <svg class="task-state" width="24" height="30" viewBox="0 0 24 30" aria-label="Start"><path d="M4 3 L20 15 L4 27 Z" fill="none" stroke="var(--accent)" stroke-width="3" stroke-linejoin="round"/></svg>
      <span class="task-name">01 TASK</span>
      <svg class="task-action action-pin" width="40" height="40" viewBox="0 0 40 40" aria-label="Pinned"><path d="M24 4 L36 16 L31 17 L24 24 L24 31 L9 16 L16 16 L23 9 Z M14 26 L4 36" fill="none" stroke="var(--accent)" stroke-width="3" stroke-linejoin="round" stroke-linecap="round"/></svg>
      <svg class="task-action action-clock" width="40" height="40" viewBox="0 0 40 40" aria-label="Reminder"><circle cx="20" cy="20" r="16" fill="none" stroke="var(--accent)" stroke-width="3"/><path d="M20 10 V20 L27 25" fill="none" stroke="var(--accent)" stroke-width="3" stroke-linecap="round"/></svg>
      <svg class="task-action action-place" width="36" height="44" viewBox="0 0 36 44" aria-label="Location"><path d="M18 41 C18 41 4 26 4 17 A14 14 0 0 1 32 17 C32 26 18 41 18 41 Z" fill="none" stroke="var(--accent)" stroke-width="3"/><circle cx="18" cy="17" r="5" fill="none" stroke="var(--accent)" stroke-width="3"/></svg>
    </li>
    <li class="task-row is-running">
      <svg class="task-state" width="26" height="26" viewBox="0 0 26 26" aria-label="Stop"><rect x="2" y="2" width="22" height="22" fill="var(--accent)"/></svg>
      <span class="task-name">01 TASK</span>
      <span class="task-timer">00:15:30</span>
      <svg class="task-action action-pin" width="40" height="40" viewBox="0 0 40 40" aria-label="Pinned"><path d="M24 4 L36 16 L31 17 L24 24 L24 31 L9 16 L16 16 L23 9 Z M14 26 L4 36" fill="none" stroke="var(--accent)" stroke-width="3" stroke-linejoin="round" stroke-linecap="round"/></svg>
      <svg class="task-action action-place" width="36" height="44" viewBox="0 0 36 44" aria-label="Location"><path d="M18 41 C18 41 4 26 4 17 A14 14 0 0 1 32 17 C32 26 18 41 18 41 Z" fill="none" stroke="var(--accent)" stroke-width="3"/><circle cx="18" cy="17" r="5" fill="none" stroke="var(--accent)" stroke-width="3"/></svg>
    </li>
    <li class="task-row">
      <svg class="task-state" width="24" height="30" viewBox="0 0 24 30" aria-label="Start"><path d="M4 3 L20 15 L4 27 Z" fill="none" stroke="var(--accent)" stroke-width="3" stroke-linejoin="round"/></svg>
      <span class="task-name">01 TASK</span>
      <svg class="task-action action-pin" width="40" height="40" viewBox="0 0 40 40" aria-label="Pinned"><path d="M24 4 L36 16 L31 17 L24 24 L24 31 L9 16 L16 16 L23 9 Z M14 26 L4 36" fill="none" stroke="var(--accent)" stroke-width="3" stroke-linejoin="round" stroke-linecap="round"/></svg>
      <svg class="task-action action-clock" width="40" height="40" viewBox="0 0 40 40" aria-label="Reminder"><circle cx="20" cy="20" r="16" fill="none" stroke="var(--accent)" stroke-width="3"/><path d="M20 10 V20 L27 25" fill="none" stroke="var(--accent)" stroke-width="3" stroke-linecap="round"/></svg>
    </li>
    <li class="task-row">
      <svg class="task-state" width="24" height="30" viewBox="0 0 24 30" aria-label="Start"><path d="M4 3 L20 15 L4 27 Z" fill="none" stroke="var(--accent)" stroke-width="3" stroke-linejoin="round"/></svg>
      <span class="task-name">01 TASK</span>
      <svg class="task-action action-pin" width="40" height="40" viewBox="0 0 40 40" aria-label="Pinned"><path d="M24 4 L36 16 L31 17 L24 24 L24 31 L9 16 L16 16 L23 9 Z M14 26 L4 36" fill="none" stroke="var(--accent)" stroke-width="3" stroke-linejoin="round" stroke-linecap="round"/></svg>
      <svg class="task-action action-place" width="36" height="44" viewBox="0 0 36 44" aria-label="Location"><path d="M18 41 C18 41 4 26 4 17 A14 14 0 0 1 32 17 C32 26 18 41 18 41 Z" fill="none" stroke="var(--accent)" stroke-width="3"/><circle cx="18" cy="17" r="5" fill="none" stroke="var(--accent)" stroke-width="3"/></svg>
    </li>
    <li class="task-row">
      <svg class="task-state" width="24" height="30" viewBox="0 0 24 30" aria-label="Start"><path d="M4 3 L20 15 L4 27 Z" fill="none" stroke="var(--accent)" stroke-width="3" stroke-linejoin="round"/></svg>
      <span class="task-name">01 TASK</span>
      <svg class="task-action action-pin" width="40" height="40" viewBox="0 0 40 40" aria-label="Pinned"><path d="M24 4 L36 16 L31 17 L24 24 L24 31 L9 16 L16 16 L23 9 Z M14 26 L4 36" fill="none" stroke="var(--accent)" stroke-width="3" stroke-linejoin="round" stroke-linecap="round"/></svg>
      <svg class="task-action action-place" width="36" height="44" viewBox="0 0 36 44" aria-label="Location"><path d="M18 41 C18 41 4 26 4 17 A14 14 0 0 1 32 17 C32 26 18 41 18 41 Z" fill="none" stroke="var(--accent)" stroke-width="3"/><circle cx="18" cy="17" r="5" fill="none" stroke="var(--accent)" stroke-width="3"/></svg>
    </li>
  </ul>

  <div class="add-button" aria-label="Add task">
    <svg width="40" height="40" viewBox="0 0 40 40" aria-hidden="true">
      <path d="M20 6 V34 M6 20 H34" stroke="var(--fab-icon)" stroke-width="4.5" stroke-linecap="round"/>
    </svg>
  </div>

</main>
</body>
</html>
```